Business Card Design

Looking for a professional looking business card for a carpentry/construction business that deals with renovations, extensions, homes, and anything carpentry based in Northern Australia. Would like to incorporate the attached logo with backgrounds of white, grey or maybe a close up of timber/wood grain. Thanks

Industry/Entity Type

Carpentry

Contact Information for Business Card

Dean Pollard, Owner, Po Box 2946 Katherine NT 0851, dean-pollard@tallmail.example, 0461907243, Builders Number: 392417CR

Requirements
Should not have
• Power tools/hand tools related to carpentry

```html
<!DOCTYPE html>
<html lang="en">
<head>
<meta charset="utf-8">
<title>Pollard Carpentry – Business Card</title>
<link rel="stylesheet" href="https://fonts.googleapis.com/css2?family=Inter:ital,wght@0,300;0,400;1,300&display=swap">
<style>
  :root {
    --card-bg: #ffffff;
    --text-blue: #1a74c4;
    --rule-blue: #2a6fc2;
    --brand-blue: #1f5aab;
  }
  html, body {
    margin: 0;
    padding: 0;
    width: 1200px;
    height: 741px;
    overflow: hidden;
    background: var(--card-bg);
  }
  .card {
    position: relative;
    width: 1200px;
    height: 741px;
    background: var(--card-bg);
    overflow: hidden;
    font-family: "Inter", "Helvetica Neue", Arial, sans-serif;
    color: var(--text-blue);
  }
  /* Content runs bottom-to-top along the card's short side */
  .face {
    position: absolute;
    left: 0;
    top: 0;
    width: 741px;
    height: 1200px;
    transform-origin: 0 0;
    transform: translateY(741px) rotate(-90deg);
  }
  .line {
    position: absolute;
    right: 85px;
    margin: 0;
    line-height: 1;
    white-space: nowrap;
    font-weight: 300;
  }
  .name { top: 64px; font-size: 52px; }
  .role { top: 114px; font-size: 30px; font-style: italic; }
  .phone { top: 293px; font-size: 29px; }
  .email { top: 345px; font-size: 29px; }
  .licence { top: 515px; font-size: 30px; }
  .postal { top: 567px; font-size: 30px; }
  .rule {
    position: absolute;
    right: 82px;
    height: 2px;
    background: var(--rule-blue);
  }
  .rule-short { top: 227px; width: 153px; }
  .rule-long { top: 452px; width: 294px; }
  .brand {
    position: absolute;
    left: 88px;
    top: 1084px;
    margin: 0;
    font-size: 27px;
    font-weight: 400;
    line-height: 1;
    white-space: nowrap;
    color: var(--brand-blue);
  }
</style>
</head>
<body>
  <div class="card">
    <div class="face">
      <p class="line name">Dean Pollard</p>
      <p class="line role">Owner</p>
      <div class="rule rule-short"></div>
      <p class="line phone">0461907243</p>
      <p class="line email">dean-pollard@tallmail.example</p>
      <div class="rule rule-long"></div>
      <p class="line licence">Builders Number: 392417CR</p>
      <p class="line postal">Po Box 2946, Katherine NT 0851</p>
      <p class="brand">Pollard Carpentry</p>
    </div>
  </div>
</body>
</html>
```